Essential Oil Blend Label Design

I need a label designed for our stress relief essential blend, Marlow's Calm.
The text for the front of the logo will be as follows:
"Marlow's Calm
All Natural Stress and Anxiety Relief
www.brightmintcare.example"
Please make the front text small enough that it will show up in a picture of the bottle with the label is applied without being cut off on the edges. For reference, the label will be 4" x 2" and will go on these bottles:
http://www.vialcrafters.example/glass-bottles/european-dropper/amber/30ml-kvr30
On one of the sides of the label I would like this text, going up the label so that you turn the bottle sideways to read it (like in the attached label):
"Contains a pure, undiluted essential oil blend"
On the other side "For use in aromatherapy"
I would like this label to incorporate elements of a lush, green garden, like the Garden of Eden. The goal is for it convey peace and relaxation.
Please also note that I have attached the label for our other product for reference. The new label should be similar in its basic design as far as where the text is present and the overall style. My one problem with the attached label, though, is that the front text is a little too large and doesn't show up all the way in a picture. (I've attached the picture of the bottle as well so you can see what I mean).
I look forward to working with you!
Peter

```html
<!DOCTYPE html>
<html lang="en">
<head>
<meta charset="utf-8">
<title>Marlow's Calm — Essential Oil Blend Label</title>
<link rel="stylesheet" href="https://fonts.googleapis.com/css2?family=Oswald:wght@300;400&family=Cormorant+Garamond:wght@500&display=swap">
<style>
  :root {
    --backdrop: #e4e5e8;
    --label-deep: #0c1a20;
    --label-mid: #13262c;
    --label-teal: #1b3639;
    --garden-green: #1f6b66;
    --garden-moss: #2f5a45;
    --gold: #c9a96a;
    --gold-light: #d8bd85;
    --gold-dark: #a98a52;
    --ivory: #e6dcc4;
  }
  * { margin: 0; padding: 0; box-sizing: border-box; }
  html, body {
    width: 1200px;
    height: 1200px;
    overflow: hidden;
    background: var(--backdrop);
  }
  .canvas {
    width: 1200px;
    height: 1200px;
    display: flex;
    align-items: center;
    justify-content: center;
  }
  .label {
    position: relative;
    width: 1000px;
    height: 500px;
    overflow: hidden;
    background:
      linear-gradient(160deg, var(--label-mid) 0%, var(--label-deep) 55%, var(--label-teal) 100%);
  }
  .label__garden {
    position: absolute;
    inset: 0;
    width: 100%;
    height: 100%;
  }
  .label__front {
    position: absolute;
    left: 50%;
    top: 0;
    width: 420px;
    height: 100%;
    transform: translateX(-50%);
    display: flex;
    flex-direction: column;
    align-items: center;
  }
  .label__tree {
    margin-top: 70px;
    width: 200px;
    height: 110px;
  }
  .label__name {
    margin-top: 40px;
    font-family: "Oswald", "Arial Narrow", sans-serif;
    font-weight: 300;
    font-size: 44px;
    letter-spacing: 0.5px;
    color: var(--gold-light);
    line-height: 1;
  }
  .label__tagline {
    margin-top: 38px;
    font-family: "Cormorant Garamond", "Times New Roman", serif;
    font-weight: 500;
    font-size: 20px;
    letter-spacing: 3px;
    line-height: 1.6;
    color: var(--ivory);
    text-align: center;
  }
  .label__url {
    margin-top: 46px;
    font-family: "Oswald", "Arial Narrow", sans-serif;
    font-weight: 400;
    font-size: 18px;
    letter-spacing: 0.5px;
    color: var(--gold);
  }
  .label__side {
    position: absolute;
    top: 0;
    height: 100%;
    display: flex;
    align-items: center;
    justify-content: center;
    writing-mode: vertical-rl;
    transform: rotate(180deg);
    font-family: "Cormorant Garamond", "Times New Roman", serif;
    font-weight: 500;
    font-size: 17px;
    letter-spacing: 2px;
    color: var(--ivory);
    white-space: nowrap;
  }
  .label__side--left { left: 90px; }
  .label__side--right { right: 90px; }
</style>
</head>
<body>
  <main class="canvas">
    <section class="label">
      <svg class="label__garden" viewBox="0 0 1000 500" preserveAspectRatio="none" role="img" aria-label="Lush dark garden foliage with tall grasses and soft teal leaf light across the label">
        <defs>
          <radialGradient id="gardenGlowLeft" cx="0.32" cy="0.3" r="0.45">
            <stop offset="0" stop-color="#1f6b66" stop-opacity="0.35"/>
            <stop offset="1" stop-color="#1f6b66" stop-opacity="0"/>
          </radialGradient>
          <radialGradient id="gardenGlowRight" cx="0.78" cy="0.75" r="0.5">
            <stop offset="0" stop-color="#2f5a45" stop-opacity="0.35"/>
            <stop offset="1" stop-color="#2f5a45" stop-opacity="0"/>
          </radialGradient>
          <linearGradient id="gardenGround" x1="0" y1="0" x2="0" y2="1">
            <stop offset="0.55" stop-color="#1f6b66" stop-opacity="0"/>
            <stop offset="1" stop-color="#1f6b66" stop-opacity="0.18"/>
          </linearGradient>
        </defs>
        <rect width="1000" height="500" fill="url(#gardenGlowLeft)"/>
        <rect width="1000" height="500" fill="url(#gardenGlowRight)"/>
        <rect width="1000" height="500" fill="url(#gardenGround)"/>
      </svg>

      <p class="label__side label__side--left">Contains a pure, undiluted essential oil blend</p>

      <div class="label__front">
        <svg class="label__tree" viewBox="0 0 200 110" role="img" aria-label="Gold illustration of a wide spreading garden tree">
          <defs>
            <radialGradient id="treeGold" cx="0.5" cy="0.45" r="0.5">
              <stop offset="0" stop-color="#d8bd85"/>
              <stop offset="0.7" stop-color="#a98a52" stop-opacity="0.7"/>
              <stop offset="1" stop-color="#a98a52" stop-opacity="0"/>
            </radialGradient>
          </defs>
          <ellipse cx="100" cy="55" rx="100" ry="55" fill="url(#treeGold)"/>
        </svg>
        <h1 class="label__name">Marlow's Calm</h1>
        <p class="label__tagline">All Natural Stress<br>and Anxiety Relief</p>
        <p class="label__url">www.brightmintcare.example</p>
      </div>

      <p class="label__side label__side--right">For use in aromatherapy</p>
    </section>
  </main>
</body>
</html>
```